Lumbrook - We create living space - needs a web/WIX design

The website will be in the German language.
During the contest, I welcome designs with English text.
I will provide the German text to the winner.
We prefer WIX-Design for the future, if possible to make the website WiX-ready;

The text to be used in the webpage:
In the project description I’ve written a text about our company in English and in German – as you asked for. Please use this text in the first step.

QUALITY, EXPERTISE and EXPERIENCE
EVERYTHING UNDER A SINGLE ROOF

We are a real estate company based in Vienna, Austria. Our company's main competences are planning, conception, development, erection, sale/renting and management of properties. "We make best quality for the best price" - with this motto LUMBROOK offers living space in high quality in Austria as well as in other countries. Thereby the working area of our property development focusses on both new construction and attic extensions.

QUALITÄT, KOMPETENZ UND ERFAHRUNG
ALLES UNTER EINEM DACH​

LUMBROOK ist ein Komplettanbieter für Wohnimmobilien von der Vision, Konzeption, Entwicklung, Planung, Errichtung und Verkauf/Vermietung bis zur Hausverwaltung. „Wir bauen beste Qualität zum besten Preis“, unter diesem Motto bietet LUMBROOK qualitativ hochwertigen, lebenswerten und nachhaltig gebauten Wohnraum sowohl in Österreich als auch in anderen Ländern an. Dabei konzentriert sich das Arbeitsfeld unserer Bauträgergesellschaft auf die beiden Kernbereiche Neubau und Dachgeschossausbau.

In the boxes “Must haves”, “Nice to haves”, “Should not haves” I’ve mentioned everything the designers need to know (font, colours etc.). AS I’ve received already some very good designs, there should be everything clear for the designers.

During the contest: homepage is welcome

Target Market(s)

Austria, Germany, Europe, Israel, USA; we would like to reach families, singles, male, female, general population and also investors

Industry/Entity Type

Real Estate Development

Number of Pages Required

5+ page

Font styles to use
Other font styles liked:
• See Upload

Colors

Designer to choose colors to be used in the design.

Requirements
Must have
• Pages called: "Company", "Projects", "Investments", "Partner", "Contact"; Link to projects; subsides (Team, News); enough space for renderings; Our company colours are yellow, grey, white and black (see our logo) - our website should be designed in this colours; Website in friendly and light colours
Nice to have
• Our company font for titles - attached; Eventually other font for the text - better readable; We prefer WIX-Design for the future, if possible to make the website WiX-ready.
• It should be clear, that the font in the attachement should be used; the provided files are pictures of our interior designs and the logo; we expect creativity from the designers, so they should use the best pictures in their opinion.
Should not have
• dark design

```html
<!DOCTYPE html>
<html lang="en">
<head>
<meta charset="utf-8">
<title>Lumbrook – We create living space</title>
<link href="https://fonts.googleapis.com/css2?family=Teko:wght@400;500;600&family=Roboto:wght@400;500;700&display=swap" rel="stylesheet">
<style>
:root{
  --yellow:#f7e51c;
  --black:#1c1c1c;
  --dark:#333335;
  --darker:#262628;
  --grey:#ececee;
  --text:#555;
  --white:#fff;
  --blue:#2f7fc1;
}
*{margin:0;padding:0;box-sizing:border-box}
html,body{width:1200px;height:2416px;overflow:hidden;background:var(--white)}
body{position:relative;font-family:'Roboto',sans-serif;color:var(--text)}
.title{font-family:'Teko',sans-serif;font-weight:500;color:var(--black);letter-spacing:1px;text-transform:uppercase}
section,header,footer{position:absolute;left:0;width:1200px}

/* header */
.site-header{top:0;height:68px;background:var(--white)}
.brand-name{position:absolute;font-family:'Roboto',sans-serif;font-size:26px;font-weight:700;line-height:1;color:var(--black)}
.site-header .brand-name{left:128px;top:21px}
.nav{position:absolute;right:128px;top:22px;display:flex;gap:6px;list-style:none}
.nav li{font-size:12px;font-weight:500;padding:6px 12px;color:var(--black)}
.nav li.active{background:var(--yellow)}

/* hero */
.hero{top:68px;height:532px}
.hero-photo{position:absolute;inset:0;background:linear-gradient(100deg,#d9d9d6 0%,#bcbcb8 35%,#e4e4e0 60%,#9d9d99 100%)}
.hero-title{position:absolute;left:200px;width:800px;top:300px;text-align:center;font-family:'Teko',sans-serif;font-weight:400;font-size:36px;line-height:36px;color:var(--white);letter-spacing:3px;text-transform:uppercase}
.hero-arrow{position:absolute;top:320px;width:28px;height:36px;background:var(--black);display:flex;align-items:center;justify-content:center}
.hero-arrow.prev{left:0}.hero-arrow.next{right:0}

/* features */
.features{top:600px;height:200px;background:var(--yellow)}
.feature{position:absolute;top:40px;width:240px;display:flex;gap:14px}
.feature svg{flex:none}
.feature h3{margin:8px 0 8px;font-family:'Teko',sans-serif;font-size:20px;font-weight:500;color:var(--black)}
.feature p{font-size:11px;line-height:16px;color:#3a3a2a}

/* about */
.about{top:800px;height:430px}
.about-text{position:absolute;left:200px;top:138px;width:420px;text-align:center}
.about-text h2{font-size:34px;line-height:32px;margin-bottom:14px}
.about-text p{font-size:11px;line-height:16px}
.about-render{position:absolute;left:840px;top:82px;width:232px;height:282px;background:linear-gradient(170deg,#e5e8ec 0%,#b9bcc0 55%,#7a8a6e 100%)}

/* services */
.services{top:1230px;height:490px;background:var(--grey)}
.section-title{position:absolute;left:0;width:1200px;text-align:center;font-size:34px}
.section-title::after{content:"";display:block;width:40px;height:3px;background:var(--yellow);margin:0 auto}
.service{position:absolute;top:170px;width:260px;text-align:center}
.service svg{display:block;margin:0 auto 26px}
.service h3{font-size:12px;font-weight:500;color:var(--black);margin-bottom:10px;text-transform:uppercase}
.service p{font-size:11px;line-height:16px;padding:0 24px}
.divider{position:absolute;top:180px;width:1px;height:200px;background:#cfcfd2}

/* partners */
.partners{top:1720px;height:310px}
.partner-badge{position:absolute;top:150px;width:110px;height:110px;background:#3a3a3a}

/* contact band */
.contact-band{top:2030px;height:90px;background:var(--yellow)}
.contact-item{position:absolute;top:24px;display:flex;gap:14px;align-items:center}
.contact-item small{display:block;font-size:11px;font-weight:500;color:var(--black);text-transform:uppercase}
.contact-item strong{display:block;font-family:'Teko',sans-serif;font-size:24px;font-weight:500;color:var(--black);line-height:24px}
.contact-sep{position:absolute;top:20px;width:1px;height:50px;background:#c9b912}

/* footer */
.site-footer{top:2120px;height:266px;background:var(--dark);color:#cfcfcf}
.site-footer .brand-name{left:160px;top:84px;color:var(--white)}
.socials{position:absolute;left:190px;top:144px;display:flex;gap:8px}
.socials span{width:22px;height:22px;border-radius:50%;background:var(--blue)}
.footer-col{position:absolute;top:80px}
.footer-col h4{font-size:11px;font-weight:500;color:var(--white);margin-bottom:12px;text-transform:uppercase}
.footer-col li{list-style:none;font-size:11px;line-height:18px}
.footer-col .line{display:flex;gap:10px;align-items:center;font-size:11px;line-height:24px}
.copyright{position:absolute;left:0;top:2386px;width:1200px;height:30px;background:var(--darker);color:#9a9a9a;font-size:10px;text-align:center;line-height:30px}
</style>
</head>
<body>

<header class="site-header">
  <span class="brand-name">Lumbrook</span>
  <ul class="nav">
    <li class="active">HOME</li><li>TEAM</li><li>NEWS</li><li>INVESTMENTS</li><li>PARTNER</li><li>CONTACT</li>
  </ul>
</header>

<section class="hero">
  <div class="hero-photo" role="img" aria-label="Bright modern living room interior with white sofa, dining table and large windows"></div>
  <h1 class="hero-title">Quality, competence and experience<br>all under one roof</h1>
  <div class="hero-arrow prev"><svg width="10" height="14" viewBox="0 0 10 14"><path d="M8 1 2 7l6 6" fill="none" stroke="#fff" stroke-width="2"/></svg></div>
  <div class="hero-arrow next"><svg width="10" height="14" viewBox="0 0 10 14"><path d="M2 1l6 6-6 6" fill="none" stroke="#fff" stroke-width="2"/></svg></div>
</section>

<section class="features">
  <div class="feature" style="left:130px">
    <svg width="40" height="34" viewBox="0 0 40 34"><circle cx="20" cy="9" r="6" fill="#1c1c1c"/><circle cx="8" cy="12" r="4.5" fill="#1c1c1c"/><circle cx="32" cy="12" r="4.5" fill="#1c1c1c"/><path d="M10 32c0-8 4-14 10-14s10 6 10 14z" fill="#1c1c1c"/><path d="M0 30c0-6 3-11 8-11 2 0 3 1 4 2-2 3-3 6-3 9zM40 30c0-6-3-11-8-11-2 0-3 1-4 2 2 3 3 6 3 9z" fill="#1c1c1c"/></svg>
    <div><h3>BEST TEAM</h3><p>It is a long established fact that a reader will be distracted by the readable content.</p></div>
  </div>
  <div class="feature" style="left:484px">
    <svg width="24" height="40" viewBox="0 0 24 40"><text x="12" y="34" text-anchor="middle" font-family="Roboto,sans-serif" font-size="36" font-weight="700" fill="#1c1c1c">$</text></svg>
    <div><h3>BEST PRICES</h3><p>It is a long established fact that a reader will be distracted by the readable content.</p></div>
  </div>
  <div class="feature" style="left:818px">
    <svg width="40" height="30" viewBox="0 0 40 30"><path d="M3 18 20 4l17 14" fill="none" stroke="#1c1c1c" stroke-width="4"/><rect x="6" y="24" width="28" height="3" fill="#1c1c1c"/></svg>
    <div><h3>ROOF FLOORING</h3><p>It is a long established fact that a reader will be distracted by the readable content.</p></div>
  </div>
</section>

<section class="about">
  <div class="about-text">
    <h2 class="title">We build the best quality<br>at the best price</h2>
    <p>LUMBROOK offers high-quality, sustainable and liveable living space in Austria as well as in other countries. The focus of our development company is on new construction and on attic extensions.</p>
  </div>
  <div class="about-render" role="img" aria-label="Architectural rendering of a modern multi-storey residential building with trees"></div>
</section>

<section class="services">
  <h2 class="title section-title" style="top:64px">Services</h2>
  <div class="service" style="left:140px">
    <svg width="46" height="40" viewBox="0 0 46 40"><path d="M2 16 23 3l21 13" fill="none" stroke="#333" stroke-width="3"/><rect x="7" y="16" width="32" height="22" fill="#333"/><rect x="12" y="21" width="6" height="5" fill="#ececee"/><rect x="20" y="21" width="6" height="5" fill="#ececee"/><rect x="28" y="21" width="6" height="5" fill="#ececee"/><rect x="12" y="29" width="6" height="5" fill="#ececee"/><rect x="28" y="29" width="6" height="5" fill="#ececee"/></svg>
    <h3>Development</h3>
    <p>Lorem ipsum is simply dummy text of the printing and typesetting industry. Lorem ipsum has been the industry's standard text.</p>
  </div>
  <div class="divider" style="left:410px"></div>
  <div class="service" style="left:470px">
    <svg width="50" height="40" viewBox="0 0 50 40"><path d="M3 22 14 12l9 5 9-5 15 10-12 10-10-6-6 4z" fill="#333"/><path d="M14 12 4 8M36 12l10-4" stroke="#333" stroke-width="3"/></svg>
    <h3>Planning</h3>
    <p>Lorem ipsum is simply dummy text of the printing and typesetting industry. Lorem ipsum has been the industry's standard text.</p>
  </div>
  <div class="divider" style="left:790px"></div>
  <div class="service" style="left:800px">
    <svg width="44" height="40" viewBox="0 0 44 42"><rect x="10" y="4" width="4" height="36" fill="#333"/><rect x="4" y="4" width="38" height="4" fill="#333"/><path d="M38 8v10" stroke="#333" stroke-width="2"/><rect x="34" y="18" width="8" height="6" fill="#333"/><rect x="20" y="26" width="14" height="14" fill="#333"/><rect x="4" y="38" width="36" height="3" fill="#333"/></svg>
    <h3>Construction</h3>
    <p>Lorem ipsum is simply dummy text of the printing and typesetting industry. Lorem ipsum has been the industry's standard text.</p>
  </div>
</section>

<section class="partners">
  <h2 class="title section-title" style="top:48px">Partners</h2>
  <div class="partner-badge" style="left:262px;height:60px;top:175px;background:#2c2c2c"></div>
  <div class="partner-badge" style="left:460px;background:#777;clip-path:polygon(50% 0,93% 25%,93% 75%,50% 100%,7% 75%,7% 25%)"></div>
  <div class="partner-badge" style="left:650px;height:70px;top:170px;background:#2c2c2c"></div>
  <div class="partner-badge" style="left:826px;border-radius:50%;width:100px;height:100px;background:#2c2c2c"></div>
</section>

<section class="contact-band">
  <div class="contact-item" style="left:160px">
    <svg width="26" height="26" viewBox="0 0 24 24"><path d="M6.6 10.8a15 15 0 0 0 6.6 6.6l2.2-2.2a1 1 0 0 1 1-.25c1.1.37 2.3.57 3.6.57a1 1 0 0 1 1 1V20a1 1 0 0 1-1 1A17 17 0 0 1 3 4a1 1 0 0 1 1-1h3.5a1 1 0 0 1 1 1c0 1.25.2 2.45.57 3.57a1 1 0 0 1-.25 1z" fill="#1c1c1c"/></svg>
    <div><small>Call us</small><strong>555.010.2040</strong></div>
  </div>
  <div class="contact-sep" style="left:428px"></div>
  <div class="contact-item" style="left:520px">
    <svg width="26" height="20" viewBox="0 0 26 20"><rect x="1" y="1" width="24" height="18" fill="none" stroke="#1c1c1c" stroke-width="2"/><path d="M1 2l12 9 12-9" fill="none" stroke="#1c1c1c" stroke-width="2"/></svg>
    <div><small>E-mail us</small><strong>info@lumbrook.com</strong></div>
  </div>
  <div class="contact-sep" style="left:768px"></div>
  <div class="contact-item" style="left:820px">
    <svg width="26" height="26" viewBox="0 0 26 26"><circle cx="13" cy="13" r="11" fill="none" stroke="#1c1c1c" stroke-width="2"/><path d="M13 6v7l5 3" fill="none" stroke="#1c1c1c" stroke-width="2"/></svg>
    <div><small>Opening hours</small><strong>Mon – Fri: 7am – 10pm</strong></div>
  </div>
</section>

<footer class="site-footer">
  <span class="brand-name">Lumbrook</span>
  <div class="socials"><span></span><span></span><span></span></div>
  <div class="footer-col" style="left:556px">
    <h4>Our services</h4>
    <ul><li>Vision</li><li>Conception</li><li>Development</li><li>Planning</li><li>Sale / Renting</li></ul>
  </div>
  <div class="footer-col" style="left:868px">
    <h4>About us</h4>
    <div class="line"><svg width="10" height="14" viewBox="0 0 10 14"><path d="M5 0a5 5 0 0 0-5 5c0 4 5 9 5 9s5-5 5-9a5 5 0 0 0-5-5z" fill="#cfcfcf"/></svg>12 Ostler Lane</div>
    <div class="line" style="padding-left:20px;margin-top:-8px">Vienna, Austria</div>
    <div class="line"><svg width="12" height="12" viewBox="0 0 24 24"><path d="M6.6 10.8a15 15 0 0 0 6.6 6.6l2.2-2.2a1 1 0 0 1 1-.25c1.1.37 2.3.57 3.6.57a1 1 0 0 1 1 1V20a1 1 0 0 1-1 1A17 17 0 0 1 3 4a1 1 0 0 1 1-1h3.5a1 1 0 0 1 1 1c0 1.25.2 2.45.57 3.57a1 1 0 0 1-.25 1z" fill="#cfcfcf"/></svg>555.010.2040</div>
    <div class="line"><svg width="12" height="10" viewBox="0 0 26 20"><rect x="1" y="1" width="24" height="18" fill="none" stroke="#cfcfcf" stroke-width="3"/><path d="M1 2l12 9 12-9" fill="none" stroke="#cfcfcf" stroke-width="3"/></svg>info@lumbrook.com</div>
  </div>
</footer>
<div class="copyright">Copyright © 2017 All Rights Reserved</div>

</body>
</html>
```